E-Book-Cover für meinen Roman Was der Nebel trägt
Sehr angenehmer Kontakt, das Beschriebene wurde auf Anhieb in die Richtung umgesetzt, die ich angestrebt habe. Änderungswünsche wurden prompt und unermüdlich umgesetzt, bis das Endergebnis stand. Sehr zu empfehlen!
Zielgruppe
Ich veröffentliche in Eigenregie meinen Roman namens 'Was der Nebel trägt' im Rahmen des Self-Publishing Angebots von Lesowa.de
Bei meinem Werk handelt es sich um Belletristik: eine Geschichte aus dem Leben, die traurige und lustige Elemente zu gleichen Teilen eint. Behandelt wird der Lebensabschnitt eines Jugendlichen, der zu früh Erfahrung mit dem Tod macht, als seine Mutter schwer erkrankt. Gleichzeitig gilt es, den (humorvoll verpackten) Alltag zu meistern, in dem er wieder und wieder auf Ablehnung und Distanz angesichts seiner ungewöhnlichen und misslichen Lage stößt. Es gelingt ihm nicht mehr, Teil seiner gleichaltrigen Mitstreiter zu werden.
Gleichzeitig gibt es einen zweiten Handlungsstrang, in dem eine ebenfalls Jugendliche ähnliche Erfahrungen macht, auch wenn die Umstände andere sind, ebenso wie die Reaktion darauf. Während der männliche Protagonist wiederholt von seinem Umkreis enttäuscht wird, stellt er sich am Ende der Prüfung, der er nicht entkommen kann. Sein weibliches Pendant hingegen tritt eine überstürzte Flucht mit ungewissem Ausgang an. Beide Stränge sind lose miteinander verwoben, und als Leser stellt man sich zusehends die Frage, ob und wann diese verbunden werden. Eine Auflösung erfolgt am Schluss.
Nach einigen Testlesern stellte sich heraus, dass jene am meisten begeistert waren, die selbst ähnliche Erfahrungen gemacht haben, wie die fiktiven Personen. Grundsätzlich lässt sich aber sagen, dass der Schreibstil, die beschriebenen Medien und Situationen eher auf (junge) Erwachsene zugeschnitten sind. Dennoch handelt es sich nicht um ein klassisches Jugendbuch, oft werden Dinge beschrieben, die für Minderjährige nicht geeignet sind. Als (Haupt)zielgruppe würde ich grob den Rahmen 20-40 Jahre vorgeben, wobei die Leser eher noch älter als jünger sein dürfen.
Aufgabenstellung
Zunächst technisch: (Angaben lt. Lesowa)
JPEG oder TIFF-Datei
mindestens 1000 Pixel an der längsten Seite
Idealverhältnis von Bildhöhe- und breite: 1,6 (Beispiel: 1000 x 1600)
bei weißen Covern sollte ein 2-3 Pixel breiter, grauer Rand hinzugefügt werden, damit sich das Cover von der Website selbst abhebt
Weiterhin zu beachten:
-Hauptsächlich wird es auf eBook Readern gelesen, die nur in Graustufen darstellen. Das Cover sollte also in jedem Fall auch in Schwarz-Weiß nichts von seiner Wirkung einbüßen!
Selbiges gilt für eine Miniaturansicht!
Autor: Matthias Krollner
Titel: Was der Nebel trägt
Zusatz: Roman
Nun zu den wichtigsten Vorgaben:
-Selbstverständlich soll das Cover Aufmerksamkeit erzeugen und neugierig machen.
-Das Thema "anders sein" / "im Abseits stehen" / "hin- und hergetrieben werden" muss auf jeden Fall rübergebracht werden, da dies auch das Kernthema des Buches ist.
-Bei der Schriftart gibt es keine bestimmte Vorgabe, nur bitte nichts in Kapitälchen oder Großbuchstaben. (z.B. WAS DER NEBEL TRÄGT)
-Es soll auf keinen Fall übertrieben ernst oder möchtegern-schnulzig rüberkommen. (Bilder vom Strand, untergehender Sonne und weitere Klischees.)
-Vielmehr darf man dem Cover bereits ansehen, dass es ein ernstes Thema auch mit Humor nehmen kann. z.B. durch Stilisierung, einfache Farben anstatt aufwändiger Realaufnahmen und Schatten, evtl. auch in Richtung Comic, aber nicht zu albern.
-Die Platzierung von Autor und Titel darf klassisch sein, gerne aber auch ungewöhnlich überraschend.
Ich habe diesem Inserat einige Entwürfe meinerseits beigefügt, wie ich das o.g. Thema stilisieren würde, z.B.:
der Querschnitt eines einfahrenden Zuges (Hauptverkehrsmittel im Buch), bei dem in allen Fenstern Licht brennt, mit Ausnahme von einem. (Hier dürfen gerne auch die Profile von Menschen hinzug..

```html
<!DOCTYPE html>
<html lang="de">
<head>
<meta charset="utf-8">
<title>Was der Nebel trägt – Matthias Krollner</title>
<link rel="stylesheet" href="https://fonts.googleapis.com/css2?family=Exo+2:wght@500;600;700&display=swap">
<style>
  :root {
    --page: #ffffff;
    --frame: #dcdcdc;
    --coral: #dd5a4a;
    --coral-soft: #e8968a;
    --rose: #d44b72;
    --rose-soft: #efb3bf;
    --ink: #111111;
  }
  html, body {
    margin: 0;
    padding: 0;
    width: 846px;
    height: 1200px;
    overflow: hidden;
    background: var(--page);
  }
  .cover {
    position: absolute;
    left: 107px;
    top: 102px;
    width: 623px;
    height: 999px;
    box-sizing: border-box;
    border: 7px solid var(--frame);
    background: var(--page);
    overflow: hidden;
    font-family: "Exo 2", sans-serif;
  }
  .cover-illustration {
    position: absolute;
    left: 0;
    top: 0;
    width: 100%;
    height: 600px;
    display: block;
  }
  .title-line,
  .genre,
  .author {
    position: absolute;
    left: 0;
    width: 100%;
    margin: 0;
    text-align: center;
    line-height: 1;
    font-weight: 700;
    letter-spacing: -0.01em;
  }
  .title { margin: 0; }
  .title-line--rose { color: var(--rose); }
  .title-line--coral { color: var(--coral); }
  .title-line--1 { top: 489px; font-size: 69px; }
  .title-line--2 { top: 555px; font-size: 72px; }
  .title-line--3 { top: 611px; font-size: 98px; letter-spacing: -0.02em; }
  .title-line--4 { top: 701px; font-size: 75px; }
  .genre {
    top: 782px;
    font-size: 28px;
    font-weight: 600;
    color: var(--coral);
  }
  .author {
    top: 852px;
    font-size: 36px;
    font-weight: 500;
    color: var(--ink);
  }
</style>
</head>
<body>
  <div class="cover">
    <svg class="cover-illustration" viewBox="0 0 609 600" preserveAspectRatio="none" role="img"
         aria-label="Gezeichnete Illustration: Bahngleise mit Oberleitungen führen in die Ferne, eine kleine Gestalt geht zwischen den Schienen, roter Himmel über rosa Feldern">
      <defs>
        <linearGradient id="sceneTone" x1="0" y1="0" x2="0" y2="1">
          <stop offset="0" stop-color="#ffffff"/>
          <stop offset="0.17" stop-color="#ffffff"/>
          <stop offset="0.2" stop-color="var(--coral)"/>
          <stop offset="0.55" stop-color="var(--coral)"/>
          <stop offset="0.6" stop-color="var(--rose-soft)"/>
          <stop offset="0.68" stop-color="var(--rose)"/>
          <stop offset="0.8" stop-color="#f1c4cf"/>
          <stop offset="1" stop-color="#ffffff"/>
        </linearGradient>
      </defs>
      <rect x="0" y="0" width="609" height="600" fill="url(#sceneTone)"/>
    </svg>

    <h1 class="title">
      <span class="title-line title-line--1 title-line--rose">Was</span>
      <span class="title-line title-line--2 title-line--rose">der</span>
      <span class="title-line title-line--3 title-line--coral">Nebel</span>
      <span class="title-line title-line--4 title-line--rose">trägt</span>
    </h1>
    <p class="genre">Roman</p>
    <p class="author">Matthias Krollner</p>
  </div>
</body>
</html>
```